Interior Design & consultancy firm requires a new business card design that is a little bit funky bu

Meridale Design Services is a leading strategic design practice specialising in the development and implementation of strategies and design solutions for commercial workplaces across a wide variety of industries.

The company has over twenty years experience in the strategic design, development and construction of innovative and efficient workplace environments for the commercial, corporate and industrial sectors.

We believe good design and efficient workspaces can transform companies, improve people’s lives and increase productivity.

Target Market(s)

My clients are mainly Government or corporate clients wanting to create a statement with their office fitout & new furniture that reflects their corporate identity

Industry/Entity Type

Construction

Font styles to use
Sans Serif

Colors
add136

Requirements
Must have
• The business card must be easy to read, simple & highlight my name & mobile phone number
Should not have
• I do not want the card to be fussy, feature too many colours or look to busy.

```html
<!DOCTYPE html>
<html lang="en">
<head>
<meta charset="UTF-8">
<title>Meridale Design Services – Business Card</title>
<link rel="stylesheet" href="https://fonts.googleapis.com/css2?family=Quicksand:wght@400;500&display=swap">
<style>
  :root {
    --page-bg: #f3f3f3;
    --card-white: #ffffff;
    --pattern-grey: #ececec;
    --brand-green: #1db34a;
    --green-light: #8dc63f;
    --green-deep: #00a85a;
    --ink: #2b2b2b;
    --ink-soft: #1f3b22;
    --text-on-green: #ffffff;
  }
  * { margin: 0; padding: 0; box-sizing: border-box; }
  html, body {
    width: 1200px;
    height: 900px;
    overflow: hidden;
  }
  body {
    background: var(--page-bg);
    font-family: "Quicksand", sans-serif;
    display: flex;
    align-items: center;
    justify-content: center;
    gap: 60px;
  }
  .card {
    width: 520px;
    height: 310px;
    border-radius: 26px;
    position: relative;
    overflow: hidden;
  }

  /* Front */
  .card-front {
    background: var(--card-white);
    padding: 8px;
  }
  .front-frame {
    width: 100%;
    height: 100%;
    border: 8px solid var(--brand-green);
    border-radius: 20px;
    position: relative;
    overflow: hidden;
  }
  .front-texture {
    position: absolute;
    inset: 0;
    background: var(--pattern-grey);
  }
  .front-brand {
    position: absolute;
    inset: 0;
    display: flex;
    flex-direction: column;
    align-items: center;
    justify-content: center;
    gap: 22px;
  }
  .brand-dot-large {
    width: 86px;
    height: 86px;
    border-radius: 50%;
    background: var(--brand-green);
  }
  .brand-name-large {
    font-size: 27px;
    font-weight: 400;
    color: var(--ink);
    letter-spacing: 0.2px;
  }

  /* Back */
  .card-back {
    background: linear-gradient(180deg, var(--green-light) 0%, #5cbf48 45%, var(--green-deep) 70%, var(--green-deep) 100%);
    display: flex;
    flex-direction: column;
    align-items: center;
    padding-top: 40px;
  }
  .brand-dot-small {
    width: 44px;
    height: 44px;
    border-radius: 50%;
    background: var(--ink-soft);
    opacity: 0.85;
  }
  .brand-name-small {
    margin-top: 10px;
    font-size: 13px;
    font-weight: 400;
    color: var(--ink);
  }
  .holder-name {
    margin-top: 30px;
    font-size: 25px;
    font-weight: 400;
    color: var(--text-on-green);
  }
  .holder-title {
    margin-top: 2px;
    font-size: 10px;
    font-weight: 500;
    color: var(--ink-soft);
  }
  .holder-mobile {
    margin-top: 28px;
    font-size: 22px;
    font-weight: 400;
    letter-spacing: 5px;
    color: var(--text-on-green);
  }
</style>
</head>
<body>
  <section class="card card-front" aria-label="Business card front">
    <div class="front-frame">
      <div class="front-texture" role="img" aria-label="Subtle light grey diamond texture background"></div>
      <div class="front-brand">
        <div class="brand-dot-large" aria-hidden="true"></div>
        <p class="brand-name-large">Meridale Design Services</p>
      </div>
    </div>
  </section>

  <section class="card card-back" aria-label="Business card back">
    <div class="brand-dot-small" aria-hidden="true"></div>
    <p class="brand-name-small">Meridale Design Services</p>
    <h1 class="holder-name">Carla Whitmore</h1>
    <p class="holder-title">Director/Senior Interior Designer</p>
    <p class="holder-mobile">0400 127 583</p>
  </section>
</body>
</html>
```